Local Flower Farm Needs Business Card Design

I need business cards designed for a flower farm based in Eudora, Kansas.
Business Info:
We are a local cut flower farm located in Eudora, Kansas, founded by Darla Hoffstrom. What started as a passion for agriculture and search for more joy in daily life has blossomed into a small business dedicated to providing the community with beautiful, fresh, and sustainable flowers. We specialize in local, seasonal blooms, ensuring that every petal reflects the care and dedication we pour into our craft. Our mission is to deliver the highest quality flowers directly to our customers through local farmers markets and to florists who share our commitment to sustainability. Join us in celebrating the beauty of nature, one bloom at a time!
Contact Details:
Darla Hoffstrom
Owner
Phone 913-555-0147
Facebook: Lorabelle Quinn Blossoms
Instagram: @LorabelleQuinnBlossoms
Website: LorabelleQuinnBlossoms.example
Target Market(s)
Wholesale to Florists and Direct to Consumer via Farmers Market
Industry/Entity Type
Florist, Farm
Contact Information for Business Card
Name, Contact Info, Logo
Look and feel

```html
<!DOCTYPE html>
<html lang="en">
<head>
<meta charset="utf-8">
<title>Lorabelle Quinn Blossoms – Business Card</title>
<link rel="stylesheet" href="https://fonts.googleapis.com/css2?family=Arimo:wght@400;700&display=swap">
<style>
  :root {
    --backdrop: #1d1f21;
    --card: #0f3337;
    --card-edge: #0b2a2d;
    --ink: #ffffff;
    --ink-soft: #d9e3e3;
    --rule: #c9d4d4;
  }
  * { margin: 0; padding: 0; box-sizing: border-box; }
  html, body {
    width: 1200px; height: 900px; overflow: hidden;
    background: var(--backdrop);
    font-family: "Arimo", Arial, sans-serif;
  }
  .canvas {
    position: relative; width: 1200px; height: 900px;
    display: flex; align-items: center; justify-content: center; gap: 40px;
  }
  .card {
    position: relative; width: 540px; height: 309px;
    background: var(--card);
    border-radius: 3px;
    box-shadow: 0 0 0 1px var(--card-edge);
    color: var(--ink);
  }
  /* front */
  .holder { position: absolute; left: 34px; top: 34px; }
  .holder-name { font-weight: 700; font-size: 19px; letter-spacing: 0.5px; text-transform: uppercase; }
  .holder-role { font-size: 11px; color: var(--ink-soft); margin-top: 3px; }
  .holder-rule { width: 160px; height: 1px; background: var(--rule); margin-top: 9px; }
  .contacts { position: absolute; left: 34px; top: 110px; list-style: none; }
  .contacts li {
    display: flex; align-items: center; gap: 7px;
    font-size: 12.5px; color: var(--ink-soft); margin-bottom: 5px;
  }
  .contacts svg, .web svg { flex: none; }
  .long-rule { position: absolute; left: 34px; right: 34px; top: 222px; height: 1px; background: var(--rule); }
  .web {
    position: absolute; left: 34px; top: 240px;
    display: flex; align-items: center; gap: 8px; font-size: 15px;
  }
  .brand {
    position: absolute; display: flex; align-items: center; gap: 10px;
  }
  .brand-mark { width: 14px; height: 14px; border: 1.5px solid var(--ink); border-radius: 50%; flex: none; }
  .brand-name { font-weight: 400; color: var(--ink); text-transform: uppercase; letter-spacing: 1.5px; line-height: 1.25; }
  .card-front .brand { right: 30px; top: 96px; }
  .card-front .brand-name { font-size: 13px; width: 120px; }
  .card-back .brand { left: 50%; top: 50%; transform: translate(-50%, -50%); }
  .card-back .brand-name { font-size: 16px; width: 150px; }
</style>
</head>
<body>
<main class="canvas">
  <section class="card card-front" aria-label="Card front">
    <div class="holder">
      <div class="holder-name">Darla Hoffstrom</div>
      <div class="holder-role">Owner</div>
      <div class="holder-rule"></div>
    </div>
    <ul class="contacts">
      <li>
        <svg width="11" height="11" viewBox="0 0 24 24" aria-hidden="true"><path fill="#fff" d="M6.6 10.8c1.4 2.8 3.8 5.1 6.6 6.6l2.2-2.2c.3-.3.7-.4 1-.2 1.1.4 2.3.6 3.6.6.6 0 1 .4 1 1V20c0 .6-.4 1-1 1C10.6 21 3 13.4 3 4c0-.6.4-1 1-1h3.5c.6 0 1 .4 1 1 0 1.3.2 2.5.6 3.6.1.3 0 .7-.2 1z"/></svg>
        913-555-0147
      </li>
      <li>
        <svg width="11" height="11" viewBox="0 0 12 12" aria-hidden="true"><circle cx="6" cy="6" r="5" fill="#fff"/></svg>
        Lorabelle Quinn Blossoms
      </li>
      <li>
        <svg width="11" height="11" viewBox="0 0 12 12" aria-hidden="true"><circle cx="6" cy="6" r="4.5" fill="none" stroke="#fff" stroke-width="1.2"/></svg>
        @LorabelleQuinnBlossoms
      </li>
    </ul>
    <div class="brand">
      <span class="brand-mark"></span>
      <span class="brand-name">Lorabelle Quinn Blossoms</span>
    </div>
    <div class="long-rule"></div>
    <div class="web">
      <svg width="13" height="13" viewBox="0 0 24 24" aria-hidden="true"><g fill="none" stroke="#fff" stroke-width="2"><circle cx="12" cy="12" r="10"/><ellipse cx="12" cy="12" rx="4" ry="10"/><path d="M2 12h20"/></g></svg>
      LorabelleQuinnBlossoms.example
    </div>
  </section>

  <section class="card card-back" aria-label="Card back">
    <div class="brand">
      <span class="brand-mark"></span>
      <span class="brand-name">Lorabelle Quinn Blossoms</span>
    </div>
  </section>
</main>
</body>
</html>
```